Company Real Estate Site Needs A Face Lift

I need a new website for the recent company I formed: Voska Real Estate.
You can use my agent website WWW.PALMIROQ.COM to see the style/brand I already have. I will have areas for Searching for homes on IDX, etc.
I really like this site:
http://www.cranfeltmanorhomes.com/
I have attached my logo as well

Industry/Entity Type

Real Estate

Colors
0255a3
ffffff
cee9f5

```html
<!DOCTYPE html>
<html lang="en">
<head>
<meta charset="utf-8">
<title>Voska Real Estate</title>
<link href="https://fonts.googleapis.com/css2?family=Jost:wght@400;500&family=Sorts+Mill+Goudy&family=Open+Sans:wght@400;600&family=Raleway:wght@400;600&display=swap" rel="stylesheet">
<style>
  :root {
    --brand-blue: #0255a3;
    --brand-blue-bright: #1f8fe0;
    --sky: #cee9f5;
    --white: #ffffff;
    --topbar: #181818;
    --footer: #232323;
    --footer-deep: #141414;
    --footer-text: #8a8a8a;
    --footer-head: #9a9a9a;
    --link: #1f7fd0;
    --ink: #333333;
    --submit: #0a7fb5;
  }
  * { margin: 0; padding: 0; box-sizing: border-box; }
  html, body { width: 1200px; height: 1060px; overflow: hidden; background: var(--white); }
  body { position: relative; font-family: Arial, Helvetica, sans-serif; }
  .abs { position: absolute; }

  /* top bar */
  .top-bar { left: 0; top: 0; width: 1200px; height: 64px; background: var(--topbar); color: var(--white); font-family: "Jost", sans-serif; }
  .top-email { left: 79px; top: 21px; font-size: 14px; letter-spacing: .2px; }
  .social { top: 24px; width: 21px; height: 21px; background: #bdbdbd; border-radius: 2px; }
  .top-link { top: 22px; font-size: 18px; color: #e8e8e8; display: flex; align-items: center; gap: 12px; }
  .top-link svg { width: 24px; height: 22px; }
  .top-phone { left: 960px; top: 22px; font-size: 18px; font-weight: 500; letter-spacing: .5px; }

  /* hero */
  .hero-photo { left: 0; top: 64px; width: 1200px; height: 578px;
    background: linear-gradient(90deg, #e9e3da 0%, #d8d2c8 35%, #cfd3d6 55%, #aeb4b8 75%, #c8c6c0 100%); }
  .hero-shade { left: 0; top: 64px; width: 1200px; height: 113px; background: rgba(28,28,28,.72); }
  .logo-plate { left: 0; top: 64px; }
  .logo { left: 62px; top: 96px; display: flex; align-items: center; gap: 10px; font-family: "Jost", sans-serif; font-weight: 500; font-size: 25px; color: var(--white); line-height: 1; }
  .logo-dot { width: 16px; height: 16px; border-radius: 50%; background: var(--brand-blue-bright); }
  .logo small { display: block; font-size: 12px; letter-spacing: 3px; margin-top: 4px; }

  .main-nav { top: 123px; left: 0; font-family: "Jost", sans-serif; font-size: 18px; color: var(--white); letter-spacing: .4px; }
  .nav-item { position: absolute; top: 7px; white-space: nowrap; }
  .nav-home { position: absolute; left: 313px; top: 0; width: 85px; height: 34px; background: var(--brand-blue); border-radius: 3px; padding: 7px 0 0 13px; }

  .panels { left: 0; top: 0; }
  .welcome-title { left: 274px; top: 224px; font-family: "Sorts Mill Goudy", serif; font-size: 28px; color: #222; }
  .welcome-copy { left: 258px; top: 269px; width: 330px; font-size: 13.4px; line-height: 20px; color: #555; text-align: center; }
  .welcome-strong { left: 256px; top: 368px; width: 320px; font-size: 13.4px; line-height: 20px; color: #111; font-weight: bold; text-align: center; }
  .cta { left: 379px; top: 421px; font-size: 14px; font-weight: bold; color: var(--brand-blue); }

  .auction-title { left: 177px; top: 515px; font-family: "Sorts Mill Goudy", serif; font-size: 27px; color: #222; }
  .auction-line { left: 172px; top: 556px; font-size: 14px; font-style: italic; font-weight: bold; color: #333; }
  .auction-date { left: 172px; top: 578px; font-size: 12.5px; font-style: italic; color: #333; }
  .auction-date b { margin-right: 5px; }
  .auction-links { left: 475px; top: 559px; font-family: "Jost", sans-serif; font-size: 13.5px; font-weight: 500; color: var(--brand-blue); line-height: 19px; }

  /* newsletter */
  .newsletter { left: 0; top: 642px; }
  .newsletter-title { left: 161px; top: 685px; font-family: "Open Sans", sans-serif; font-size: 20px; color: #333; }
  .field { top: 732px; height: 28px; border: 1px solid #d0d0d0; border-radius: 3px; background: var(--white);
    box-shadow: inset 0 2px 3px rgba(0,0,0,.12); font-family: "Open Sans", sans-serif; font-size: 12.5px; color: #999; padding: 6px 12px; }
  .submit { left: 997px; top: 733px; width: 89px; height: 28px; background: var(--submit); color: var(--white); border-radius: 2px;
    font-family: "Open Sans", sans-serif; font-weight: 600; font-size: 14px; text-align: center; line-height: 28px; }

  /* footer */
  .footer { left: 0; top: 802px; width: 1200px; height: 222px; background-color: var(--footer);
    background-image: repeating-linear-gradient(45deg, rgba(255,255,255,.025) 0 1px, transparent 1px 4px); border-top: 2px solid #e8e8e8; }
  .footer-head { top: 819px; font-family: "Open Sans", sans-serif; font-weight: 600; font-size: 14px; color: var(--footer-head); }
  .testimonial { left: 138px; top: 851px; width: 280px; font-family: "Raleway", sans-serif; font-size: 13.4px; line-height: 19px; color: var(--footer-text); }
  .post-thumb { left: 466px; width: 79px; height: 38px; }
  .post-date { left: 556px; font-family: "Raleway", sans-serif; font-size: 11px; color: #999; }
  .post-link { left: 556px; width: 210px; font-family: "Raleway", sans-serif; font-size: 11.5px; line-height: 18px; color: var(--link); }
  .contact { left: 797px; font-family: "Raleway", sans-serif; font-size: 14px; line-height: 22px; color: var(--footer-text); display: flex; gap: 14px; }
  .contact svg { width: 16px; height: 16px; margin-top: 3px; flex: none; }
  .contact a { color: var(--link); text-decoration: none; }
  .contact-rule { left: 790px; top: 1018px; width: 300px; height: 1px; background: #444; }

  .copyright { left: 0; top: 1024px; width: 1200px; height: 36px; background: var(--footer-deep); color: #999; font-size: 13px; text-align: center; line-height: 38px; }

  .blue-sweep { left: 0; top: 0; pointer-events: none; }
</style>
</head>
<body>

<header class="abs top-bar">
  <div class="abs top-email">Email us at : hello@voskahomes.com</div>
  <span class="abs social" style="left:575px" aria-label="Social link"></span>
  <span class="abs social" style="left:605px" aria-label="Social link"></span>
  <span class="abs social" style="left:636px" aria-label="Social link"></span>
  <div class="abs top-link" style="left:695px">
    <svg viewBox="0 0 24 22"><rect x="3" y="2" width="18" height="18" fill="none" stroke="#aaa" stroke-width="2"/><path d="M7 7h10M7 11h10M7 15h7" stroke="#aaa" stroke-width="2"/></svg>NEWS
  </div>
  <div class="abs top-link" style="left:814px">
    <svg viewBox="0 0 24 22"><rect x="3" y="3" width="18" height="16" fill="none" stroke="#aaa" stroke-width="2"/><path d="M6 16l5-6 4 4 3-3 2 5z" fill="#aaa"/></svg>GALLERY
  </div>
  <div class="abs top-phone">1-800-482-9170</div>
</header>

<div class="abs hero-photo" role="img" aria-label="Photo of a bright living room with a white sofa and side table before tall windows overlooking a city skyline"></div>
<div class="abs hero-shade"></div>

<svg class="abs logo-plate" width="320" height="113" viewBox="0 0 320 113">
  <defs><linearGradient id="plate" x1="0" y1="0" x2="1" y2="1"><stop offset="0" stop-color="#9a9a9a"/><stop offset=".5" stop-color="#d6d6d6"/><stop offset="1" stop-color="#8c8c8c"/></linearGradient></defs>
  <polygon points="0,0 318,0 280,113 0,113" fill="url(#plate)"/>
</svg>
<div class="abs logo"><span class="logo-dot"></span><div>VOSKA<small>REAL ESTATE</small></div></div>

<nav class="abs main-nav">
  <div class="nav-home">HOME</div>
  <span class="nav-item" style="left:431px">AUCTIONS</span>
  <span class="nav-item" style="left:543px">SERVICES</span>
  <span class="nav-item" style="left:644px">FOR SALE</span>
  <span class="nav-item" style="left:749px">ABOUT US</span>
  <span class="nav-item" style="left:858px">EVENTS</span>
  <span class="nav-item" style="left:945px">CONTACT US</span>
</nav>

<svg class="abs panels" width="1200" height="642" viewBox="0 0 1200 642">
  <polygon points="240,207 701,207 576,486 170,486" fill="rgba(255,255,255,.72)"/>
  <polygon points="140,506 617,506 562,620 120,620" fill="rgba(255,255,255,.8)"/>
</svg>

<section>
  <h1 class="abs welcome-title" style="font-weight:400">Welcome To Voska...</h1>
  <p class="abs welcome-copy">atque corrupti quos dolores et quas molestias dignissi-mos ducimus qui blanditiis praesentium voluptatum deleniti atque corrupti quos dolores et quas molestias excepturi sint occaecati cupiditate non provident, simi</p>
  <p class="abs welcome-strong">At vero eos et accusamus et iusto odio dignissi-mos ducimus qui blanditiis praesentium</p>
  <a class="abs cta">List your Property Now &gt;</a>
</section>

<section>
  <h2 class="abs auction-title" style="font-weight:400">Upcoming Auctions</h2>
  <p class="abs auction-line">Live On-site Auction With Online Bidding</p>
  <p class="abs auction-date"><b>Begins:</b>Tuesday, April 23, 2013 at 10:00 AM EDT</p>
  <div class="abs auction-links">Details &#8250;<br>Photos &#8250;</div>
</section>

<svg class="abs newsletter" width="1200" height="160" viewBox="0 0 1200 160">
  <defs><linearGradient id="news" x1="0" y1="0" x2="0" y2="1"><stop offset="0" stop-color="#ffffff"/><stop offset="1" stop-color="#dcdde0"/></linearGradient></defs>
  <polygon points="148,32 1200,32 1200,160 100,160" fill="url(#news)" stroke="#e2e4e8"/>
</svg>
<h3 class="abs newsletter-title" style="font-weight:400">Subscribe to our Newsletter</h3>
<div class="abs field" style="left:162px;width:288px">Name:</div>
<div class="abs field" style="left:461px;width:278px">Email:</div>
<div class="abs field" style="left:754px;width:210px">Phone :</div>
<div class="abs submit">Submit</div>

<footer class="abs footer"></footer>
<h4 class="abs footer-head" style="left:138px">Our Customers Say:</h4>
<h4 class="abs footer-head" style="left:463px">Featured</h4>
<h4 class="abs footer-head" style="left:792px">Get in touch</h4>

<p class="abs testimonial">Lorem Ipsum is simply dummy text of the printing and typesetting industry. Lorem Ipsum has been the industry's standard dummy text ever since the 1500s, when an unknown printer took a galley of type and scrambled it to make a type specimen book. It has survived not only five centuries,</p>

<div class="abs post-thumb" style="top:852px;background:linear-gradient(180deg,#b9cde0,#e8ecef 60%,#6d7a6a)" role="img" aria-label="Photo of a white modern house"></div>
<div class="abs post-date" style="top:851px">December 3,2013</div>
<div class="abs post-link" style="top:864px">Nulla varius commodo</div>

<div class="abs post-thumb" style="top:911px;background:linear-gradient(180deg,#4d8fd0,#c9bfa8 60%,#6f7c55)" role="img" aria-label="Photo of a family home under a blue sky"></div>
<div class="abs post-date" style="top:910px">December 1,2013</div>
<div class="abs post-link" style="top:924px">Nulla varius commodo</div>

<div class="abs post-thumb" style="top:970px;background:linear-gradient(180deg,#5a9ad6,#a88a74 55%,#5f6d4c)" role="img" aria-label="Photo of a brick house with gables"></div>
<div class="abs post-date" style="top:969px">December 1,2013</div>
<div class="abs post-link" style="top:982px">This is an amazing Image Post for everyone</div>

<div class="abs contact" style="top:852px">
  <svg viewBox="0 0 16 16"><path d="M3 1v14M3 2h8l-2 3 2 3H3" fill="none" stroke="#999" stroke-width="2"/></svg>
  <div style="margin-left:2px">Harlow Point Offices<br>1187 Fenwick Ridge Rd, Suite 210<br>Dalmore, OR 97342</div>
</div>
<div class="abs contact" style="top:941px">
  <svg viewBox="0 0 16 16"><path d="M4 1l3 3-2 2c1 2 3 4 5 5l2-2 3 3-2 3C7 14 2 9 1 3z" fill="#999"/></svg>
  <div>+(41) 708 224 3196</div>
</div>
<div class="abs contact" style="top:985px">
  <svg viewBox="0 0 16 16"><rect x="1" y="3" width="14" height="10" fill="#999"/><path d="M1 3l7 6 7-6" fill="none" stroke="#232323" stroke-width="1.5"/></svg>
  <a>desk@voskahomes.com</a>
</div>
<div class="abs contact-rule"></div>

<div class="abs copyright">© 2014 Copyright - Voska Real Estate . All rights reserved</div>

<svg class="abs blue-sweep" width="300" height="1060" viewBox="0 0 300 1060">
  <defs>
    <radialGradient id="sweep" cx="0.15" cy="0.3" r="0.9"><stop offset="0" stop-color="#3aa8f5"/><stop offset=".45" stop-color="#0f72cc"/><stop offset="1" stop-color="#0255a3"/></radialGradient>
  </defs>
  <polygon points="0,177 280,177 0,960" fill="url(#sweep)"/>
</svg>

</body>
</html>
```